Business card design for Plumbing and Gas fitting company

We need a business card design for our plumbing and gas fitting company using the company logo and director details. Design should be modern and eye-catching however kept reasonably simple. This design should be targeted at commercial businesses/work so professionalism is key.

Target Market(s)

Commercial/business

Industry/Entity Type

Plumbing

Contact Information for Business Card

Warwick Tane
Director
027 815 0937
warwick@harbourlinepipeworks.example
PO Box 8716
Palmerston North 4441

Font styles to use
Sans Serif

Requirements
Must have
• Logo
• Modern
• Kept simple
Nice to have
• Colour scheme based around logo

```html
<!DOCTYPE html>
<html lang="en">
<head>
<meta charset="utf-8">
<title>Harbourline Pipeworks – Business Card</title>
<link rel="stylesheet" href="https://fonts.googleapis.com/css2?family=Open+Sans:wght@400;600;700&display=swap">
<style>
  :root {
    --bg: #2b2b2d;
    --brand-blue: #0b74bd;
    --brand-orange: #ee7b2f;
    --ink-grey: #7a7a7a;
    --ink-dark: #555;
    --card-white: #ffffff;
  }
  * { margin: 0; padding: 0; box-sizing: border-box; }
  html, body {
    width: 1200px; height: 880px; overflow: hidden;
    background: var(--bg);
    font-family: "Open Sans", sans-serif;
  }
  .stage {
    position: relative; width: 1200px; height: 880px;
  }
  .card {
    position: absolute;
    width: 560px; height: 320px;
    border-radius: 22px;
    overflow: hidden;
    box-shadow: 0 18px 40px rgba(0,0,0,.45);
  }
  /* front */
  .card-front {
    left: 110px; top: 90px;
    background: var(--brand-blue);
    display: flex; align-items: center; justify-content: center;
  }
  .brand {
    display: flex; align-items: center; gap: 14px;
  }
  .brand-dot {
    width: 34px; height: 34px; border-radius: 50%;
  }
  .brand-name {
    font-weight: 700; font-size: 34px; letter-spacing: .5px; line-height: 1;
  }
  .card-front .brand-dot { background: #fff; }
  .card-front .brand-name { color: #fff; }

  /* back */
  .card-back {
    left: 530px; top: 470px;
    background: var(--card-white);
  }
  .edge-accent {
    position: absolute; left: -20px; top: 168px;
    width: 40px; height: 40px; border-radius: 50%;
    background: var(--brand-orange);
  }
  .card-back .brand {
    position: absolute; right: 34px; top: 42px;
  }
  .card-back .brand-dot { background: var(--brand-orange); width: 26px; height: 26px; }
  .card-back .brand-name { color: var(--ink-grey); font-size: 28px; }

  .person {
    position: absolute; left: 44px; top: 150px;
  }
  .person-name {
    color: var(--brand-blue); font-weight: 600; font-size: 20px; text-transform: uppercase; letter-spacing: .3px;
  }
  .person-role {
    color: var(--ink-grey); font-size: 15px; margin-top: 1px;
  }
  .contacts {
    position: absolute; left: 44px; bottom: 30px;
    list-style: none;
    color: var(--ink-dark); font-size: 13.5px;
  }
  .contacts li { display: flex; align-items: center; gap: 9px; height: 21px; }
  .contacts svg { width: 15px; height: 15px; flex: none; }
  .address {
    position: absolute; right: 34px; bottom: 34px;
    text-align: right; color: var(--ink-grey); font-size: 14px; line-height: 1.45;
  }
</style>
</head>
<body>
<main class="stage">

  <section class="card card-front" aria-label="Card front">
    <div class="brand">
      <span class="brand-dot"></span>
      <span class="brand-name">Harbourline Pipeworks</span>
    </div>
  </section>

  <section class="card card-back" aria-label="Card back">
    <span class="edge-accent"></span>

    <div class="brand">
      <span class="brand-dot"></span>
      <span class="brand-name">Harbourline Pipeworks</span>
    </div>

    <div class="person">
      <p class="person-name">Warwick Tane</p>
      <p class="person-role">Founder/Director</p>
    </div>

    <ul class="contacts">
      <li>
        <svg viewBox="0 0 16 16" aria-hidden="true"><rect width="16" height="16" rx="2" fill="#ee7b2f"/><rect x="5" y="3" width="6" height="10" rx="1" fill="none" stroke="#fff" stroke-width="1.3"/><circle cx="8" cy="11" r=".8" fill="#fff"/></svg>
        027 815 0937
      </li>
      <li>
        <svg viewBox="0 0 16 16" aria-hidden="true"><rect width="16" height="16" rx="2" fill="#ee7b2f"/><path d="M3 6c0-1.5 2.5-2.5 5-2.5s5 1 5 2.5v1h-3V6H6v1H3z" fill="#fff"/><rect x="4" y="8" width="8" height="5" rx="1" fill="#fff"/></svg>
        027 427 3628
      </li>
      <li>
        <svg viewBox="0 0 16 16" aria-hidden="true"><rect width="16" height="16" rx="2" fill="#ee7b2f"/><rect x="3" y="4.5" width="10" height="7" fill="none" stroke="#fff" stroke-width="1.2"/><path d="M3 4.5l5 4 5-4" fill="none" stroke="#fff" stroke-width="1.2"/></svg>
        warwick@harbourlinepipeworks.example
      </li>
      <li>
        <svg viewBox="0 0 16 16" aria-hidden="true"><rect width="16" height="16" rx="2" fill="#ee7b2f"/><circle cx="8" cy="8" r="5" fill="none" stroke="#fff" stroke-width="1.1"/><path d="M3 8h10M8 3c-2.5 3-2.5 7 0 10M8 3c2.5 3 2.5 7 0 10" fill="none" stroke="#fff" stroke-width="1"/></svg>
        www.harbourlinepipeworks.example
      </li>
    </ul>

    <address class="address">
      PO Box 8716<br>
      Palmerston North 4441
    </address>
  </section>

</main>
</body>
</html>
```